Business Card & Full Stationary design For Summit Quarry
Summit Quarry For Marble & Granite
Business Card & Full Stationary design For Summit Quarry  - Construction
Creative Brief
Professional
Eng. Karim Haddouri
C.E.O
14 Shari' Nakhil el Wadi, Rawdatein, Giza, 12487, Egypt
kbh@summitquarry.com.eg
www.summitquarry.com.eg
we need everything to be included in the design ( CD, CD Cover, Letterhead, Envelopes, portfolio cover, etc..)
q7rimo q7rimo
I would highly appreciate if you can provide your concepts showing all the required stationaries including the back side of the B.Card ( Letterhead, 2 size envelope, Portfolio cover, CD, CD cover, Backgrounds for smartphones and Computers .)
Vonto Vonto

```html
<!DOCTYPE html>
<html lang="en">
<head>
<meta charset="utf-8">
<title>Summit Quarry – Business Card</title>
<link href="https://fonts.googleapis.com/css2?family=Montserrat:wght@400;500;600&display=swap" rel="stylesheet">
<style>
  :root {
    --backdrop: #e4e2df;
    --sand: #cbbda6;
    --slate: #7c7777;
    --slate-dark: #6a6565;
    --pearl: #f4f4f3;
    --pearl-shade: #d9d9d8;
    --ink: #3e3b3a;
    --gold: #a89a7f;
  }
  html, body {
    margin: 0;
    width: 1200px;
    height: 802px;
    overflow: hidden;
    background: var(--backdrop);
    font-family: "Montserrat", sans-serif;
  }
  .canvas {
    position: relative;
    width: 1200px;
    height: 802px;
  }
  .card {
    position: absolute;
    top: 251px;
    width: 520px;
    height: 300px;
    box-shadow: 0 6px 18px rgba(0,0,0,.18);
    overflow: hidden;
  }
  .card--front { left: 50px; }
  .card--back  { left: 630px; }
  .card svg { position: absolute; inset: 0; }

  .brand {
    position: absolute;
    left: 150px;
    top: 92px;
    color: var(--gold);
    text-align: center;
  }
  .brand__name {
    font-size: 30px;
    font-weight: 400;
    letter-spacing: 1px;
  }
  .brand__tag {
    font-size: 9px;
    letter-spacing: 2px;
    text-transform: uppercase;
    margin-top: 2px;
  }
  .website {
    position: absolute;
    left: 270px;
    top: 177px;
    width: 230px;
    text-align: center;
    color: #fff;
    font-size: 13px;
    letter-spacing: .5px;
  }
  .contacts {
    position: absolute;
    left: 24px;
    top: 210px;
    color: var(--ink);
    font-size: 11px;
    line-height: 15px;
  }
  .contact {
    display: flex;
    align-items: flex-start;
    gap: 8px;
    margin-bottom: 7px;
  }
  .contact svg { position: static; flex: none; margin-top: 1px; }
  .email {
    position: absolute;
    right: 22px;
    bottom: 18px;
    display: flex;
    align-items: center;
    gap: 8px;
    color: var(--ink);
    font-size: 13px;
  }
  .email svg { position: static; }

  .person {
    position: absolute;
    left: 70px;
    top: 46px;
    color: var(--ink);
  }
  .person__name {
    font-size: 17px;
    font-weight: 500;
    letter-spacing: 1px;
    text-transform: uppercase;
  }
  .person__role {
    font-size: 11px;
    margin-top: 3px;
  }
</style>
</head>
<body>
<main class="canvas">

  <section class="card card--front">
    <svg width="520" height="300" viewBox="0 0 520 300" aria-hidden="true">
      <defs>
        <linearGradient id="pearl" x1="0" y1="0" x2="1" y2="1">
          <stop offset="0" stop-color="#ffffff"/>
          <stop offset=".6" stop-color="var(--pearl)"/>
          <stop offset="1" stop-color="var(--pearl-shade)"/>
        </linearGradient>
      </defs>
      <rect width="520" height="300" fill="var(--sand)"/>
      <rect width="520" height="70" fill="var(--slate)"/>
      <path d="M0 42 H420 Q445 42 452 62 L462 92 Q468 108 488 110 Q512 112 512 136 V170 H250 Q236 170 236 184 V196 H0 Z" fill="url(#pearl)"/>
      <rect x="250" y="170" width="262" height="36" rx="18" fill="var(--slate)"/>
    </svg>

    <div class="brand">
      <div class="brand__name">Summit Quarry</div>
      <div class="brand__tag">Marble &amp; Granite</div>
    </div>

    <div class="website">www.summitquarry.com.eg</div>

    <div class="contacts">
      <div class="contact">
        <svg width="12" height="14" viewBox="0 0 12 14" aria-hidden="true"><path d="M3 0 L5 3 L3.5 5 Q5 8.5 8 10 L10 8.5 L12 11 L10 13.5 Q3 12 0 3 Z" fill="var(--ink)"/></svg>
        <span>012 480 3157<br>012 480 3162</span>
      </div>
      <div class="contact">
        <svg width="14" height="12" viewBox="0 0 14 12" aria-hidden="true"><path d="M7 0 L14 6 H12 V12 H8.5 V8 H5.5 V12 H2 V6 H0 Z" fill="var(--ink)"/></svg>
        <span>14 Shari' Nakhil el Wadi<br>Rawdatein, Giza</span>
      </div>
    </div>

    <div class="email">
      <svg width="18" height="13" viewBox="0 0 18 13" aria-hidden="true"><rect x=".75" y=".75" width="16.5" height="11.5" fill="none" stroke="var(--ink)" stroke-width="1.5"/><path d="M1 1 L9 7.5 L17 1" fill="none" stroke="var(--ink)" stroke-width="1.5"/></svg>
      <span>kbh@summitquarry.com.eg</span>
    </div>
  </section>

  <section class="card card--back">
    <svg width="520" height="300" viewBox="0 0 520 300" aria-hidden="true">
      <defs>
        <linearGradient id="pearl-back" x1="0" y1="0" x2="1" y2="1">
          <stop offset="0" stop-color="#ffffff"/>
          <stop offset="1" stop-color="var(--pearl-shade)"/>
        </linearGradient>
      </defs>
      <rect width="520" height="300" fill="var(--sand)"/>
      <path d="M0 160 Q120 140 190 170 Q240 190 300 172 Q380 148 520 182 V262 Q420 238 340 262 Q250 288 170 258 Q90 232 0 250 Z" fill="var(--slate)"/>
      <path d="M232 150 Q248 128 290 128 H360 Q392 128 396 152 L402 210 Q404 236 378 238 H268 Q240 238 236 212 Z" fill="url(#pearl-back)"/>
    </svg>

    <div class="person">
      <div class="person__name">Karim Haddouri</div>
      <div class="person__role">Managing Director</div>
    </div>
  </section>

</main>
</body>
</html>
```